Business Card Design

I need a business card for my rental business. The business is named:
Hire a Vorlatrike Brenmoor
www.hireavorlatrikebrenmoor.example
(555) 014-2937
This will be a business card that I will leave at other businesses as advertisement so it needs to have the name, website, and phone number.
Please feel free to be creative. This is a new business so I have no designs.
Thank you very much for your time and I look forward to receiving your designs
Target Market(s)
Local rental customers
Industry/Entity Type
Business
Contact Information for Business Card
Please check out my website:
Other font styles liked:
- anything creative
Colors
Designer to choose colors to be used in the design.
Requirements
Must have
- Business name, phone, website. Rentals available hourly or daily. Book online

```html
<!DOCTYPE html>
<html lang="en">
<head>
<meta charset="utf-8">
<title>Hire a Vorlatrike Brenmoor – Business Card</title>
<link rel="stylesheet" href="https://fonts.googleapis.com/css2?family=Roboto+Slab:wght@700&family=Open+Sans:wght@300;400&family=Gochi+Hand&display=swap">
<style>
  :root {
    --page: #eceef0;
    --red-deep: #5e0d0f;
    --red-mid: #a3151a;
    --red-bright: #e01b22;
    --paper-top: #ffffff;
    --paper-bottom: #d9d9db;
    --ink-grey: #6b6b6b;
    --badge: #2a2a2a;
    --white: #ffffff;
  }
  html, body {
    margin: 0;
    width: 1200px;
    height: 478px;
    overflow: hidden;
    background: var(--page);
  }
  .canvas {
    position: relative;
    width: 1200px;
    height: 478px;
  }
  .card {
    position: absolute;
    top: 42px;
    height: 336px;
    overflow: hidden;
  }
  .card--front { left: 24px; width: 556px; }
  .card--back { left: 634px; width: 554px; }
  .divider {
    position: absolute;
    left: 582px;
    top: 42px;
    width: 50px;
    height: 336px;
    background: var(--white);
    border-radius: 4px;
  }
  .card svg { position: absolute; inset: 0; }

  .business-name {
    position: absolute;
    left: 8px;
    top: 136px;
    margin: 0;
    font: 700 17px/1 "Roboto Slab", serif;
    color: var(--ink-grey);
  }
  .phone-number {
    position: absolute;
    left: 362px;
    top: 146px;
    margin: 0;
    font: 400 28px/1 "Open Sans", sans-serif;
    color: var(--white);
  }
  .website {
    position: absolute;
    left: 28px;
    top: 303px;
    margin: 0;
    font: 400 14px/1 "Open Sans", sans-serif;
    color: var(--white);
  }

  .brand-mark {
    position: absolute;
    left: 200px;
    top: 64px;
    width: 88px;
    height: 88px;
    border-radius: 50%;
    background: var(--white);
  }
  .brand-name {
    position: absolute;
    left: 0;
    right: 0;
    top: 180px;
    margin: 0;
    text-align: center;
    font: 400 46px/1 "Gochi Hand", cursive;
    letter-spacing: 3px;
    text-transform: uppercase;
    color: var(--white);
  }
  .tagline {
    position: absolute;
    left: 0;
    right: 0;
    top: 303px;
    margin: 0;
    text-align: center;
    font: 400 15px/1 "Gochi Hand", cursive;
    word-spacing: 14px;
    color: var(--white);
  }
  .tagline-dots {
    position: absolute;
    left: 0;
    right: 0;
    top: 318px;
    margin: 0;
    text-align: center;
    font: 700 14px/1 "Open Sans", sans-serif;
    color: var(--white);
  }
</style>
</head>
<body>
<main class="canvas">

  <section class="card card--front" aria-label="Business card front">
    <svg width="556" height="336" viewBox="0 0 556 336">
      <defs>
        <linearGradient id="paper" x1="0" y1="0" x2="0" y2="1">
          <stop offset="0" stop-color="var(--paper-top)"/>
          <stop offset="1" stop-color="var(--paper-bottom)"/>
        </linearGradient>
        <linearGradient id="redField" x1="0" y1="0" x2="1" y2="1">
          <stop offset="0" stop-color="var(--red-mid)"/>
          <stop offset="0.45" stop-color="var(--red-bright)"/>
          <stop offset="1" stop-color="var(--red-deep)"/>
        </linearGradient>
        <linearGradient id="webBand" x1="0" y1="0" x2="1" y2="0">
          <stop offset="0" stop-color="var(--red-deep)"/>
          <stop offset="0.6" stop-color="var(--red-mid)"/>
          <stop offset="1" stop-color="var(--red-deep)"/>
        </linearGradient>
      </defs>
      <rect class="paper-field" width="556" height="336" fill="url(#paper)"/>
      <polygon class="red-field" role="img" aria-label="Red low-poly faceted background"
               points="326,0 556,0 556,336 300,336 300,296 236,222" fill="url(#redField)"/>
      <polygon class="red-field-edge" points="326,0 336,0 248,222 310,296 300,296 236,222" fill="var(--paper-bottom)" opacity="0.7"/>
      <rect class="web-band" x="0" y="294" width="302" height="42" fill="url(#webBand)"/>
      <polygon class="phone-badge" points="256,134 366,134 352,184 242,184" fill="var(--badge)"/>
      <circle cx="296" cy="159" r="16" fill="none" stroke="var(--white)" stroke-width="2"/>
      <path class="phone-icon" d="M289 151 q2 -2 4 0 l2 3 q1 2 -1 3 l-1 1 q2 4 6 6 l1 -1 q1 -2 3 -1 l3 2 q2 2 0 4 l-2 2 q-4 2 -11 -5 q-7 -7 -5 -11 z" fill="var(--white)"/>
    </svg>
    <h1 class="business-name">Hire a Vorlatrike Brenmoor</h1>
    <p class="phone-number">(555) 014-2937</p>
    <p class="website">www.hireavorlatrikebrenmoor.example</p>
  </section>

  <div class="divider" aria-hidden="true"></div>

  <section class="card card--back" aria-label="Business card back">
    <svg width="554" height="336" viewBox="0 0 554 336">
      <defs>
        <radialGradient id="redBack" cx="0.45" cy="0.45" r="0.8">
          <stop offset="0" stop-color="var(--red-bright)"/>
          <stop offset="0.55" stop-color="var(--red-mid)"/>
          <stop offset="1" stop-color="var(--red-deep)"/>
        </radialGradient>
      </defs>
      <rect class="red-field" role="img" aria-label="Red low-poly faceted background" width="554" height="336" fill="url(#redBack)"/>
    </svg>
    <span class="brand-mark" aria-hidden="true"></span>
    <h2 class="brand-name">Vorlatrike</h2>
    <p class="tagline">Shot your dream with vorlatrike</p>
    <p class="tagline-dots">...</p>
  </section>

</main>
</body>
</html>
```